Corvane Hollis Landing Page

We need a landing page re-designed for a new website www.corvanehollis.com and the website is live if you search the address provided.
We need the industry standard files for embedding this into the landing page of our website. The company is a real estate advisory firm, we provide professional property services and are focused on business rates (commercial property taxation in the UK).
We have uploaded a file which is meant to provide a visual guide as to how we envisage the landing page looking. You are free to come up with an entirely different creative design. The image at the top with the search button is taken from another website so the design will need to be distinctly different but may follow the same theme. Furthermore, the colour palette does not need to be followed slavishly and can be modified changed and improved upon. It might be that you want to incorporate other visual cues such as a desktop PC, laptop and Vexa as these are devices the website will be accessed from; however, this is not essential and only a guide.
**To clarify, please note, the target industry is commercial properties and not residential or domestic property, so please when incorporating designs of buildings its important to focus on commercial property such as shops, offices, industrial buildings etc.**
Occupiers of commercial real estate in the UK who pay property tax to occupy the property.

```html
<!DOCTYPE html>
<html lang="en">
<head>
<meta charset="utf-8">
<title>Corvane Hollis – Business Rates Valuations</title>
<link href="https://fonts.googleapis.com/css2?family=Open+Sans:wght@400;600;700;800&display=swap" rel="stylesheet">
<style>
:root{
  --navy:#02224a;
  --navy-deep:#011c3e;
  --orange:#f47b20;
  --card:#f2f3f5;
  --white:#ffffff;
  --text-navy:#0b2550;
  --line:#1e2f4d;
}
*{box-sizing:border-box;margin:0;padding:0}
html,body{width:677px;height:1200px;overflow:hidden;background:var(--white)}
body{font-family:"Open Sans",Arial,sans-serif;color:var(--text-navy);position:relative}
.abs{position:absolute}

/* header */
.site-header{left:0;top:0;width:677px;height:50px;background:var(--white)}
.brand{left:33px;top:15px;display:flex;align-items:center;gap:5px}
.brand-mark{width:16px;height:16px;background:var(--orange)}
.brand-name{font-weight:700;font-size:10px;color:#1a1a1a;letter-spacing:.2px}
.divider{left:143px;top:12px;width:1px;height:26px;background:#222}
.badge{left:158px;top:15px;width:46px;height:19px;border-radius:3px;background:#2b2b2b}
.nav-link{top:17px;font-size:9.5px;color:var(--text-navy);display:flex;align-items:center;gap:4px}
.nav-login{left:479px}
.nav-register{left:525px}
.btn-contact{left:589px;top:12px;width:64px;height:25px;border-radius:3px;background:var(--orange);color:var(--white);font-weight:700;font-size:8px;display:flex;align-items:center;justify-content:center;letter-spacing:.2px}

/* hero */
.hero{left:0;top:50px;width:677px;height:675px;background:var(--navy)}
.hero-photo{left:0;top:50px;width:677px;height:500px;
  background:linear-gradient(180deg,#8e9fb3 0%,#6d8299 22%,#3d5571 50%,#1b3457 78%,var(--navy) 100%)}
.hero-title{left:0;top:94px;width:677px;text-align:center;color:var(--white);font-weight:800;font-size:18px;letter-spacing:.2px;text-shadow:0 1px 3px rgba(0,0,0,.35)}
.hero-sub{left:0;top:124px;width:677px;text-align:center;color:var(--white);font-weight:700;font-size:11px;line-height:16.5px;text-shadow:0 1px 3px rgba(0,0,0,.4)}
.search{left:89px;top:203px;width:498px;height:25px;display:flex}
.search-input{flex:1;background:var(--white);font-size:10px;color:#8a8f98;padding-left:5px;display:flex;align-items:center}
.search-btn{width:101px;background:var(--orange);color:var(--white);font-weight:700;font-size:8.5px;display:flex;align-items:center;justify-content:center}
.help-title{left:0;top:302px;width:677px;text-align:center;color:var(--white);font-weight:600;font-size:25px;text-shadow:0 1px 4px rgba(0,0,0,.35)}
.card{top:367px;width:144px;height:176px;background:var(--card);border-radius:5px}
.card-icon{position:absolute;left:45px;top:22px;width:54px;height:54px;border-radius:50%;background:var(--orange);display:flex;align-items:center;justify-content:center}
.card-text{position:absolute;top:87px;font-size:7px;line-height:9px;color:var(--text-navy);white-space:nowrap}
.card-1 .card-text{left:15px}
.card-2 .card-text{left:15px}
.card-3 .card-text{left:15px}
.card-1{left:84px}.card-2{left:266px}.card-3{left:448px}
.covered-title{left:84px;top:586px;color:var(--white);font-weight:700;font-size:20px}
.covered-text{left:84px;top:630px;color:var(--white);font-size:10.5px;line-height:12px;white-space:nowrap}
.shield{left:529px;top:596px}

/* fees */
.fees-title{left:84px;top:768px;color:var(--text-navy);font-weight:800;font-size:20.5px}
.fees-text{left:84px;top:808px;font-size:10.5px;line-height:12px;white-space:nowrap}
.fees-note{left:84px;top:903px;font-size:10.5px;white-space:nowrap}

/* cta band */
.cta-band{left:0;top:964px;width:677px;height:50px;background:var(--navy-deep)}
.cta-text{left:84px;top:980px;color:var(--white);font-size:13px}
.btn-book{left:479px;top:974px;width:114px;height:30px;border-radius:3px;background:var(--orange);color:var(--white);font-weight:700;font-size:10px;display:flex;align-items:center;justify-content:center;letter-spacing:.3px}

/* footer */
.footer-nav{left:84px;top:1035px;width:509px;display:flex;justify-content:space-between;font-size:10.5px;color:var(--text-navy)}
.footer-rule{left:84px;top:1072px;width:509px;height:1px;background:var(--line)}
.socials{left:0;top:1105px;width:677px;display:flex;justify-content:center;gap:26px;font-weight:700;font-size:11px;color:var(--orange)}
.legal{left:0;top:1139px;width:677px;text-align:center;font-size:10.5px;line-height:12px;color:var(--text-navy)}
.legal b{font-weight:700}
</style>
</head>
<body>

<header class="site-header abs">
  <div class="brand abs"><span class="brand-mark"></span><span class="brand-name">Corvane Hollis</span></div>
  <div class="divider abs"></div>
  <div class="badge abs" aria-label="Accreditation badge"></div>
  <a class="nav-link nav-login abs">
    <svg width="6" height="10" viewBox="0 0 6 10"><circle cx="3" cy="2" r="1.6" fill="none" stroke="#f47b20" stroke-width="1"/><path d="M3 3.6V9.5M3 7h1.5M3 8.6h1.5" stroke="#f47b20" stroke-width="1"/></svg>Login</a>
  <a class="nav-link nav-register abs">
    <svg width="10" height="10" viewBox="0 0 10 10"><circle cx="4" cy="3" r="2.3" fill="#f47b20"/><path d="M0 9.5a4 4 0 0 1 8 0z" fill="#f47b20"/><circle cx="8" cy="7.6" r="1.8" fill="#fff" stroke="#f47b20" stroke-width=".8"/></svg>Register</a>
  <a class="btn-contact abs">CONTACT US</a>
</header>

<section class="hero abs"></section>
<div class="hero-photo abs" role="img" aria-label="Upward view of glass office towers against a cloudy sky"></div>
<h1 class="hero-title abs">DO YOU THINK YOUR BUSINESS RATES ARE TOO HIGH?</h1>
<p class="hero-sub abs">Use our free valuation tool or book a valuation with one of our qualified surveyors.<br>No shock commissions and fair fixed fees starting from £295!</p>
<div class="search abs">
  <div class="search-input">Commercial property postcode...</div>
  <div class="search-btn">Get free valuation!</div>
</div>

<h2 class="help-title abs">Need help?</h2>

<div class="card card-1 abs">
  <div class="card-icon">
    <svg width="30" height="26" viewBox="0 0 30 26"><rect x="2" y="2" width="26" height="16" rx="1.5" fill="none" stroke="#fff" stroke-width="2.4"/><path d="M11 22h8M15 18v4M8 24h14" stroke="#fff" stroke-width="2.2"/><path d="M11.5 10l2.5 2.5 4.5-5" fill="none" stroke="#fff" stroke-width="2"/></svg>
  </div>
  <p class="card-text">We pride ourselves on working<br>collaboratively with our clients.<br>That’s why we offer a free online<br>valuation tool which will help you<br>better understand your rateable<br>valuation and rates payable.</p>
</div>
<div class="card card-2 abs">
  <div class="card-icon">
    <svg width="34" height="30" viewBox="0 0 34 30"><g fill="#fff"><circle cx="12" cy="19" r="7"/><circle cx="21" cy="7" r="4"/><circle cx="27" cy="15" r="4"/></g><g stroke="#fff" stroke-width="3"><path d="M12 9.5v19M2.5 19h19M5.3 12.3l13.4 13.4M18.7 12.3L5.3 25.7"/><path d="M21 1.5v11M15.5 7h11M27 9.5v11M21.5 15h11" stroke-width="2"/></g><g fill="#f47b20"><circle cx="12" cy="19" r="2.8"/><circle cx="21" cy="7" r="1.5"/><circle cx="27" cy="15" r="1.5"/></g></svg>
  </div>
  <p class="card-text">Use our free valuation tool to<br>estimate the rateable value of<br>your commercial property in<br>England and Wales. You can add,<br>remove or alter the property<br>information, make allowances<br>and set the base rate pricing.</p>
</div>
<div class="card card-3 abs">
  <div class="card-icon">
    <svg width="32" height="32" viewBox="0 0 32 32"><path d="M16 3a13 13 0 1 1-12.6 16" fill="none" stroke="#fff" stroke-width="2.6"/><path d="M5 9c-2 3 0 9 5 14s11 7 14 5l-4-5-3 2c-2-1-5-4-6-6l2-3z" fill="#fff"/><path d="M14 14l3.5 3.5 7-7" fill="none" stroke="#fff" stroke-width="2.6"/></svg>
  </div>
  <p class="card-text">Book a qualified surveyor to<br>advise you on the rateable value<br>of your commercial property.<br>You can book an essential<br>desktop based valuation or a<br>detailed on-site valuation.</p>
</div>

<h2 class="covered-title abs">We’ve got you covered!</h2>
<p class="covered-text abs">Our rating list contains the most up-to-date information of around 2 million<br>commercial properties in England and Wales.Our qualified rating surveyors provide<br>nationwide coverage and we employ some of the highest qualified surveyors with<br>some holding the Varnell Rating Diploma.</p>
<svg class="shield abs" width="64" height="78" viewBox="0 0 64 78"><path d="M32 3L60 10v24c0 18-12 32-28 41C16 66 4 52 4 34V10z" fill="none" stroke="#fff" stroke-width="5" stroke-linejoin="round"/><path d="M18 36l10 10 18-20" fill="none" stroke="#fff" stroke-width="6" stroke-linecap="round" stroke-linejoin="round"/></svg>

<h2 class="fees-title abs">Fair fixed fees and no shock commissions!</h2>
<p class="fees-text abs">Our fees are fixed up front, ensuring there are no surprises and we promise to never charge<br>any shock commissions. Not only does this provide you with certainty of cost, it also provides you<br>with confidence that our surveyors are not lead by the prospect of large commission payments.<br>We are here from initial point of contact right through to the end, be that to provide an essential<br>desktop valuation, on-site valuation or helping you through the Check, Challenge and Appeal process.<br>We’re here to support you every step of the way.</p>
<p class="fees-note abs">Our surveyors don’t do speculative appeals, we provide honest and professional advice at a fair fixed fee.</p>

<section class="cta-band abs"></section>
<p class="cta-text abs">Book a rateable valuation with one of our surveyors!</p>
<a class="btn-book abs">BOOK VALUATION</a>

<nav class="footer-nav abs">
  <a>Pricing Plans</a><a>Discover</a><a>About</a><a>Contact</a><a>FAQs</a><a>Legal &amp; Terms</a>
</nav>
<div class="footer-rule abs"></div>
<div class="socials abs"><a>Linkora</a><a>Facelane</a><a>Chirper</a></div>
<p class="legal abs"><b>Company Registration Number:</b> 40718256<br><b>Company Registered Address:</b> Harbour Court, Quayside Park, Leeds LS9 4QT<br>© 2019 All Rights Reserved</p>

</body>
</html>
```